Harwell Construct, LLC Business Card
Business Car Design
Harwell Construct, LLC Business Card - Construction
Creative Brief
Professional
Tom Morrow
Owner
P.O. Box 5817 Carden Point, SC 29990
tmorrow@harwellconstructsc.example
www.harwellconstructsc.example
Back of Business Card should be just the logo that fills up the page.

```html
<!DOCTYPE html>
<html lang="en">
<head>
<meta charset="utf-8">
<title>Harwell Construct, LLC Business Card</title>
<link rel="stylesheet" href="https://fonts.googleapis.com/css2?family=Crimson+Text:wght@400;600;700&display=swap">
<style>
  :root {
    --backdrop: #2b2b2d;
    --card: #ffffff;
    --brand-brown: #3d2a1e;
    --ink: #2e2a27;
    --ink-soft: #55504b;
    --rule: #b9b4ae;
  }
  * { margin: 0; padding: 0; box-sizing: border-box; }
  html, body {
    width: 1200px;
    height: 780px;
    overflow: hidden;
    background: var(--backdrop);
  }
  .stage {
    position: relative;
    width: 1200px;
    height: 780px;
  }
  .business-card {
    position: absolute;
    left: 110px;
    top: 105px;
    width: 980px;
    height: 570px;
    background: var(--card);
    border-radius: 36px;
    box-shadow: 0 14px 40px rgba(0, 0, 0, 0.45);
    font-family: "Crimson Text", Georgia, serif;
    color: var(--ink);
  }
  .brand-block {
    position: absolute;
    left: 60px;
    top: 190px;
    width: 380px;
    display: flex;
    flex-direction: column;
    align-items: center;
  }
  .brand-square {
    width: 160px;
    height: 125px;
    border: 3px solid var(--brand-brown);
    margin-bottom: 22px;
  }
  .brand-name {
    font-size: 38px;
    font-weight: 700;
    color: var(--brand-brown);
    letter-spacing: 0.5px;
    text-align: center;
    line-height: 1.05;
    white-space: nowrap;
  }
  .identity {
    position: absolute;
    left: 500px;
    top: 105px;
  }
  .person-name {
    font-size: 36px;
    font-weight: 700;
    color: var(--ink);
    line-height: 1.1;
  }
  .person-role {
    font-size: 25px;
    color: var(--ink-soft);
    margin-top: 2px;
  }
  .divider {
    position: absolute;
    left: 488px;
    top: 205px;
    width: 2px;
    height: 210px;
    background: var(--rule);
  }
  .contact-block {
    position: absolute;
    left: 515px;
    top: 210px;
    font-size: 24px;
    line-height: 1.2;
    color: var(--ink);
  }
  .address { margin-bottom: 22px; }
  .contact-line {
    display: flex;
    align-items: center;
    gap: 12px;
    height: 32px;
    white-space: nowrap;
  }
  .contact-icon {
    width: 20px;
    height: 20px;
    flex: none;
    color: var(--ink-soft);
  }
</style>
</head>
<body>
<div class="stage">
  <section class="business-card">
    <div class="brand-block">
      <div class="brand-square"></div>
      <div class="brand-name">Harwell Construct</div>
    </div>

    <div class="identity">
      <div class="person-name">Tom Morrow</div>
      <div class="person-role">Owner</div>
    </div>

    <div class="divider"></div>

    <div class="contact-block">
      <div class="address">P.O. Box 5817<br>Carden Point, SC 29990</div>

      <div class="contact-line">
        <svg class="contact-icon" viewBox="0 0 20 20" aria-hidden="true">
          <path d="M5 2 L8 2 L9 6 L7 8 Q9 12 12 13 L14 11 L18 12 L18 15 Q18 18 15 18 Q3 16 2 5 Q2 2 5 2 Z" fill="currentColor"/>
        </svg>
        <span>843-555-0172</span>
      </div>
      <div class="contact-line">
        <svg class="contact-icon" viewBox="0 0 20 20" aria-hidden="true">
          <rect x="5" y="1" width="10" height="18" rx="2" fill="none" stroke="currentColor" stroke-width="2"/>
          <rect x="7" y="4" width="6" height="8" fill="currentColor"/>
          <circle cx="10" cy="15.5" r="1.3" fill="currentColor"/>
        </svg>
        <span>912-555-0148</span>
      </div>
      <div class="contact-line">
        <svg class="contact-icon" viewBox="0 0 20 20" aria-hidden="true">
          <circle cx="10" cy="10" r="3.5" fill="none" stroke="currentColor" stroke-width="2"/>
          <path d="M13.5 7 L13.5 11.5 Q13.5 14 16 14 Q18.5 14 18.5 10 A8.5 8.5 0 1 0 14 17.5" fill="none" stroke="currentColor" stroke-width="2"/>
        </svg>
        <span>tmorrow@harwellconstructsc.example</span>
      </div>
      <div class="contact-line">
        <svg class="contact-icon" viewBox="0 0 20 20" aria-hidden="true">
          <circle cx="10" cy="10" r="8.5" fill="none" stroke="currentColor" stroke-width="1.8"/>
          <ellipse cx="10" cy="10" rx="3.8" ry="8.5" fill="none" stroke="currentColor" stroke-width="1.5"/>
          <line x1="1.5" y1="10" x2="18.5" y2="10" stroke="currentColor" stroke-width="1.5"/>
        </svg>
        <span>www.harwellconstructsc.example</span>
      </div>
    </div>
  </section>
</div>
</body>
</html>
```